Body therapist needs a business card

I need a card for my business which is teaching trainings in body therapy, the company is called Wexcombe Educational Group. I teach to massage therapists around Australia, South East Asia and the USA. I am attaching my logo which will guide you as to what colours I would like to have you consider. Please consult my website to find out more about what I do. www.corvantela.com.au

My name is Daniel Wexcombe. My phone number is (03) 9417 2608 or 0461753208. email is info@corvantela.com.au

```html
<!DOCTYPE html>
<html lang="en">
<head>
<meta charset="utf-8">
<title>Wexcombe Educational Group – Business Card</title>
<link rel="stylesheet" href="https://fonts.googleapis.com/css2?family=Open+Sans:wght@400;600&family=Roboto:wght@400;700&display=swap">
<style>
  :root {
    --page: #e9e9e9;
    --brown-dark: #7a3d0e;
    --brown-light: #9c5c1e;
    --brown-text: #7b3f12;
    --lime: #c4d300;
    --red: #b80f17;
    --white: #ffffff;
    --ink: #3a3a3a;
  }
  * { margin: 0; padding: 0; box-sizing: border-box; }
  html, body { width: 1200px; height: 960px; overflow: hidden; }
  body {
    background: var(--page);
    position: relative;
    font-family: "Open Sans", Arial, sans-serif;
  }
  .card {
    position: absolute;
    width: 620px;
    height: 354px;
    overflow: hidden;
    box-shadow: 0 6px 18px rgba(0,0,0,0.18);
  }

  /* Back of card */
  .card-back {
    left: 100px; top: 100px;
    background: linear-gradient(135deg, var(--brown-dark), var(--brown-light));
  }
  .card-back .brand {
    position: absolute;
    left: 150px; top: 138px;
    display: flex; align-items: center; gap: 16px;
  }
  .card-back .brand-dot {
    width: 54px; height: 54px; border-radius: 50%;
    background: var(--lime);
  }
  .card-back .brand-name {
    color: var(--white);
    font-size: 27px; font-weight: 400;
    line-height: 1.15;
    width: 260px;
  }
  .card-back .website {
    position: absolute;
    left: 0; right: 0; bottom: 44px;
    text-align: center;
    color: var(--white);
    font-size: 14px;
    letter-spacing: 3px;
  }

  /* Front of card */
  .card-front {
    left: 480px; top: 480px;
    background: var(--white);
  }
  .band-lime {
    position: absolute;
    left: 0; top: 142px;
    width: 378px; height: 78px;
    background: var(--lime);
  }
  .band-red {
    position: absolute;
    left: 400px; top: 40px;
    width: 220px; height: 82px;
    background: var(--red);
  }
  .front-dot {
    position: absolute;
    left: 340px; top: 82px;
    width: 96px; height: 96px; border-radius: 50%;
    background: var(--brown-text);
    border: 7px solid var(--white);
  }
  .band-lime .brand-name {
    position: absolute;
    left: 58px; top: 14px;
    color: var(--brown-text);
    font-size: 22px; font-weight: 400;
    line-height: 1.1;
    width: 260px;
  }
  .person {
    position: absolute;
    left: 168px; top: 236px;
    font-family: "Roboto", Arial, sans-serif;
  }
  .person-name {
    color: var(--brown-text);
    font-weight: 700;
    font-size: 19px;
    margin-bottom: 6px;
  }
  .contact-list { list-style: none; }
  .contact-list li {
    display: flex; align-items: center; gap: 7px;
    color: var(--ink);
    font-size: 15px;
    line-height: 20px;
  }
  .contact-list svg { width: 11px; height: 11px; fill: var(--brown-text); flex: none; }
</style>
</head>
<body>

  <section class="card card-back" aria-label="Card back">
    <div class="brand">
      <span class="brand-dot"></span>
      <span class="brand-name">Wexcombe Educational Group</span>
    </div>
    <p class="website">www.corvantela.com.au</p>
  </section>

  <section class="card card-front" aria-label="Card front">
    <div class="band-red"></div>
    <div class="band-lime">
      <span class="brand-name">Wexcombe Educational Group</span>
    </div>
    <span class="front-dot"></span>

    <div class="person">
      <p class="person-name">Daniel Wexcombe</p>
      <ul class="contact-list">
        <li>
          <svg viewBox="0 0 24 24" aria-hidden="true"><path d="M6.6 10.8a15.1 15.1 0 0 0 6.6 6.6l2.2-2.2c.3-.3.7-.4 1-.2 1.1.4 2.3.6 3.6.6.6 0 1 .4 1 1V20c0 .6-.4 1-1 1A17 17 0 0 1 3 4c0-.6.4-1 1-1h3.5c.6 0 1 .4 1 1 0 1.3.2 2.5.6 3.6.1.3 0 .7-.2 1z"/></svg>
          (03) 9417 2608
        </li>
        <li>
          <svg viewBox="0 0 24 24" aria-hidden="true"><path d="M6.6 10.8a15.1 15.1 0 0 0 6.6 6.6l2.2-2.2c.3-.3.7-.4 1-.2 1.1.4 2.3.6 3.6.6.6 0 1 .4 1 1V20c0 .6-.4 1-1 1A17 17 0 0 1 3 4c0-.6.4-1 1-1h3.5c.6 0 1 .4 1 1 0 1.3.2 2.5.6 3.6.1.3 0 .7-.2 1z"/></svg>
          0461753208
        </li>
        <li>
          <svg viewBox="0 0 24 24" aria-hidden="true"><path d="M2 5h20v14H2zM3.5 6.5 12 13l8.5-6.5z"/></svg>
          info@corvantela.com.au
        </li>
        <li>
          <svg viewBox="0 0 24 24" aria-hidden="true"><circle cx="12" cy="12" r="10"/></svg>
          corvantela.com.au
        </li>
      </ul>
    </div>
  </section>

</body>
</html>
```